Pediatric Occupational Therapy Brochure Design

This design really needs to stand out, especially with all the wordage that I have included. These brochures will be given to doctors, future clients, and caregivers. I have included the logo on by brochure, so incorporating the same or similar colors would be fantastic. A trifold brochure would probably be best to fit all the information, as this is a new business and needs to convey all the information in a way that people will read.

Target Market(s)

Doctor's offices and caregivers of children with disabilities.

Industry/Entity Type

Health Care

Font styles to use
Serif
Sans Serif

Colors
33a6d7
85acd3
ffffff
33b8a4
86cfc7

Requirements
Must have
• I would like the same colors of the logo incorporated in the brochure design.
Nice to have
• I would like to see the butterfly somehow in the background or used in the design. Also a trifold or two page design would be greatly appreciated as long as the information can fit.

```html
<!DOCTYPE html>
<html lang="en">
<head>
<meta charset="UTF-8">
<title>Pediatric Occupational Therapy Services</title>
<link rel="stylesheet" href="https://fonts.googleapis.com/css2?family=Tinos:wght@400;700&family=Arimo:wght@400;700&display=swap">
<style>
  :root {
    --sky: #33a6d7;
    --sky-light: #5fbdf0;
    --mint: #4ff08c;
    --owner-bg: #c9e6f8;
    --role-bg: #a9f2c6;
    --pill: #ffff00;
    --title: #7a2fa8;
    --aqua-panel: #a6f1ea;
    --teal: #33b8a4;
    --teal-soft: #86cfc7;
    --parent-bg: #3fd6c6;
    --ink: #111111;
    --white: #ffffff;
  }
  html, body { margin: 0; padding: 0; overflow: hidden; }
  body { width: 1200px; height: 850px; }
  .brochure {
    position: relative; width: 1200px; height: 850px; overflow: hidden;
    background: linear-gradient(180deg, var(--sky-light) 0%, #6cc4f0 35%, #5fe6a6 70%, var(--mint) 100%);
  }
  .brochure__side {
    position: absolute; left: 781px; top: 0; width: 419px; height: 850px;
    background: linear-gradient(160deg, #5ad6f5 0%, #8fe7f0 40%, #6fe0d0 75%, #5ad8b8 100%);
  }
  .panel { position: absolute; box-sizing: border-box; }
  .owner {
    left: 11px; top: 21px; width: 371px; height: 328px;
    background: var(--owner-bg);
    font-family: "Tinos", "Times New Roman", serif; font-weight: 700;
    font-size: 16.5px; line-height: 1.16; color: var(--ink); padding: 12px 6px;
  }
  .owner__head { display: flex; align-items: flex-start; gap: 10px; margin-bottom: 4px; }
  .owner__mark { width: 34px; height: 34px; border-radius: 50%; background: var(--teal); flex: none; }
  .owner__name { text-align: center; padding-top: 14px; }
  .owner p { margin: 0; }
  .role-pill {
    left: 36px; top: 368px; width: 316px; height: 53px;
    background: var(--pill); border-radius: 14px;
    font-family: "Arimo", Arial, sans-serif; font-weight: 700; font-size: 16px;
    display: flex; align-items: center; justify-content: center; color: var(--ink);
  }
  .role {
    left: 11px; top: 430px; width: 371px; height: 375px;
    background: var(--role-bg);
    font-family: "Tinos", "Times New Roman", serif; font-weight: 700;
    font-size: 18px; line-height: 1.2; text-align: center; color: var(--ink);
    padding: 30px 22px;
  }
  .role p { margin: 0; }
  .title {
    position: absolute; left: 420px; top: 18px; width: 340px; margin: 0;
    font-family: "Tinos", "Times New Roman", serif; font-weight: 700;
    font-size: 31px; line-height: 1.15; text-align: center; color: var(--title);
  }
  .goals {
    left: 406px; top: 164px; width: 349px; height: 548px;
    background: rgba(210, 240, 250, 0.45); border-radius: 8px;
    font-family: "Arimo", Arial, sans-serif; font-weight: 700;
    font-size: 16.5px; line-height: 1.17; text-align: center; color: var(--ink);
    padding: 18px 8px;
  }
  .goals p { margin: 0; }
  .goals ul { list-style: none; margin: 0; padding: 0; }
  .goals li::before { content: "\2022"; }
  .conditions {
    left: 791px; top: 14px; width: 399px; height: 468px;
    background: var(--aqua-panel); border-radius: 6px;
    font-family: "Arimo", Arial, sans-serif; font-weight: 700; color: var(--ink);
    padding: 10px 26px 10px 34px;
  }
  .conditions h2 { margin: 0 0 22px; font-size: 16px; text-align: center; line-height: 1.2; }
  .conditions ul { list-style: none; margin: 0; padding: 0; font-size: 17.5px; line-height: 1.27; }
  .conditions li::before { content: "\2022"; }
  .parents {
    left: 798px; top: 530px; width: 385px; height: 299px;
    background: var(--parent-bg); border-radius: 10px;
    font-family: "Arimo", Arial, sans-serif; font-size: 17.5px; line-height: 1.3;
    color: var(--white); text-align: center; padding: 18px 24px;
  }
  .parents p { margin: 0; }
</style>
</head>
<body>
<main class="brochure">
  <div class="brochure__side"></div>

  <section class="panel owner">
    <div class="owner__head">
      <span class="owner__mark"></span>
      <div class="owner__name">Marisol Arvizu, OTR, C/NDT<br>Owner</div>
    </div>
    <p>My name is Marisol and I am a pediatric Occupational Therapist. I was born and raised in the Rio Grande Valley and have provided services to the pediatric and adult population since 2012. I am currently certified in Neuro-Developmental Treatment of Children with Cerebral Palsy and Other Neuromotor Disorders and have had the pleasure of working with children with various disorders and disabilities. I am a dedicated OTR that works with each client and family to develop a specific plan of care to maximize functional ability across all environments.</p>
  </section>

  <div class="panel role-pill">Role of Occupational Therapy with Children</div>

  <section class="panel role">
    <p>Occupational therapists work with children, who have challenges, to fully participate in normal daily activities. Those challenges may be due to developmental delay, ADD/ADHD, autism, chromosomal differences, injury, trauma, and many others. An occupational therapist evaluates to assess areas of difficulty as well as strengths, and treat the child based on his or her specific needs.</p>
  </section>

  <h1 class="title">Pediatric Occupational Therapy Services</h1>

  <section class="panel goals">
    <p>Occupational Therapy Goals<br>A child’s occupation is to be a kid! Through the use of play, I can help children acquire the skills needed for the job of living. These include, but are not limited to:</p>
    <ul>
      <li>Promoting independence in daily living skills- including dress, grooming, and feeding</li>
      <li>Facilitating developmental play skills</li>
      <li>Improving fine motor and eye-hand coordination skills</li>
      <li>Improving sensory processing skills such as organization, self-regulation and behavioral state</li>
      <li>Improving visual motor/visual perceptual skills including writing and coloring</li>
      <li>Addressing orthopedic complications and helping to increase function through the use of splinting and taping</li>
      <li>Improving balance and coordination skills through play</li>
    </ul>
  </section>

  <section class="panel conditions">
    <h2>Conditions that may benefit from Occupational Therapy:</h2>
    <ul>
      <li>ADD/ADHD</li>
      <li>Auditory Processing Disorders</li>
      <li>Autism Spectrum Disorders</li>
      <li>Cancer/Leukemia</li>
      <li>Cerebral Palsy</li>
      <li>Congenital Heart Disease</li>
      <li>Developmental Delay</li>
      <li>Failure to Thrive</li>
      <li>Genetic Disorders/Birth Defects</li>
      <li>Hemophilia</li>
      <li>Neurological Disorders</li>
      <li>Orthopedic injuries or Surgery</li>
      <li>Sensory Integration Disorders</li>
      <li>Trauma Brain Injuries</li>
      <li>Tracheostomy and/or ventilator dependency</li>
      <li>And any condition that affects a child’s growth and development</li>
    </ul>
  </section>

  <section class="panel parents">
    <p>Parental Involvement:<br>Each child’s success is strongly dependent upon the caregiver’s involvement. Therapy does not stop when the session ends and must be carried over across all environments in a child’s life. I specialize in working with parents and caregivers to ensure home programs are in place to make each child’s progress the best.</p>
  </section>
</main>
</body>
</html>
```